Logo for Internal Medicine practice

I want a logo for my Internal Medicine practice, I would like it to be with my name on it which is Lucía Barrenechea Ruiz.

I would like the business card to say the following (it is in Spanish since my practice is in Spanish):

Lucía Barrenechea Ruiz
Medicina Interna
Cel. 5583617204
luciabarrenechearuiz@correovela.mx

Logo Text

Lucía Barrenechea

```html
<!DOCTYPE html>
<html lang="es">
<head>
<meta charset="utf-8">
<title>Lucía Barrenechea Ruiz — Medicina Interna</title>
<link href="https://fonts.googleapis.com/css2?family=Josefin+Sans:wght@600&family=Questrial&display=swap" rel="stylesheet">
<style>
  :root {
    --stage: #5a6063;
    --card-dark: #000000;
    --card-light: #ffffff;
    --ink-on-dark: #c9c9c9;
    --ink-on-light: #2a2a2a;
    --accent-orange: #f28a1e;
    --accent-teal: #3f8580;
  }
  * { margin: 0; padding: 0; box-sizing: border-box; }
  html, body {
    width: 1200px; height: 1000px; overflow: hidden;
    background: var(--stage);
  }
  .canvas { position: relative; width: 1200px; height: 1000px; }
  .card {
    position: absolute;
    display: flex; flex-direction: column; align-items: center;
  }
  .card--dark {
    left: 115px; top: 83px; width: 721px; height: 396px;
    background: var(--card-dark); color: var(--ink-on-dark);
  }
  .card--light {
    left: 386px; top: 528px; width: 711px; height: 391px;
    background: var(--card-light); color: var(--ink-on-light);
  }
  .brand {
    display: flex; align-items: center; gap: 12px;
    font-family: "Josefin Sans", sans-serif; font-weight: 600;
    font-size: 22px; letter-spacing: 2px; text-transform: uppercase;
  }
  .card--dark .brand { margin-top: 140px; }
  .card--light .brand { margin-top: 137px; }
  .brand__dot {
    width: 18px; height: 18px; border-radius: 50%;
    background: var(--accent-orange);
  }
  .identity { text-align: center; font-family: "Josefin Sans", sans-serif; font-weight: 600; }
  .card--dark .identity { margin-top: 62px; }
  .card--light .identity { margin-top: 65px; }
  .identity__name { font-size: 24px; letter-spacing: 2.4px; text-transform: uppercase; }
  .identity__role { margin-top: 9px; font-size: 11px; letter-spacing: 3px; text-transform: uppercase; }
  .contact {
    position: absolute; left: 32px; right: 24px;
    display: flex; align-items: center;
    font-family: "Questrial", sans-serif; font-size: 20px;
  }
  .card--dark .contact { top: 340px; }
  .card--light .contact { top: 336px; }
  .contact__item { display: flex; align-items: center; gap: 12px; }
  .contact__item--email { position: absolute; }
  .card--dark .contact__item--email { left: 257px; }
  .card--light .contact__item--email { left: 258px; }
  .icon { fill: currentColor; flex: none; }
</style>
</head>
<body>
<main class="canvas">

  <section class="card card--dark">
    <div class="brand"><span class="brand__dot"></span>Lucía Barrenechea</div>
    <div class="identity">
      <h1 class="identity__name">Lucía Barrenechea Ruiz</h1>
      <p class="identity__role">Medicina Interna</p>
    </div>
    <div class="contact">
      <span class="contact__item">
        <svg class="icon" width="22" height="22" viewBox="0 0 24 24"><path d="M6.6 10.8a15.1 15.1 0 0 0 6.6 6.6l2.2-2.2c.3-.3.7-.4 1-.2 1.1.4 2.3.6 3.6.6.6 0 1 .4 1 1V20c0 .6-.4 1-1 1A17 17 0 0 1 3 4c0-.6.4-1 1-1h3.5c.6 0 1 .4 1 1 0 1.3.2 2.5.6 3.6.1.3 0 .7-.2 1z"/></svg>
        5583617204
      </span>
      <span class="contact__item contact__item--email">
        <svg class="icon" width="26" height="18" viewBox="0 0 26 18"><path d="M0 0h26v18H0z M2 2v.6l11 8 11-8V2z M2 5v11h22V5l-11 8z" fill-rule="evenodd"/></svg>
        luciabarrenechearuiz@correovela.mx
      </span>
    </div>
  </section>

  <section class="card card--light">
    <div class="brand"><span class="brand__dot"></span>Lucía Barrenechea</div>
    <div class="identity">
      <h2 class="identity__name">Lucía Barrenechea Ruiz</h2>
      <p class="identity__role">Medicina Interna</p>
    </div>
    <div class="contact">
      <span class="contact__item">
        <svg class="icon" width="22" height="22" viewBox="0 0 24 24"><path d="M6.6 10.8a15.1 15.1 0 0 0 6.6 6.6l2.2-2.2c.3-.3.7-.4 1-.2 1.1.4 2.3.6 3.6.6.6 0 1 .4 1 1V20c0 .6-.4 1-1 1A17 17 0 0 1 3 4c0-.6.4-1 1-1h3.5c.6 0 1 .4 1 1 0 1.3.2 2.5.6 3.6.1.3 0 .7-.2 1z"/></svg>
        5583617204
      </span>
      <span class="contact__item contact__item--email">
        <svg class="icon" width="26" height="18" viewBox="0 0 26 18"><path d="M0 0h26v18H0z M2 2v.6l11 8 11-8V2z M2 5v11h22V5l-11 8z" fill-rule="evenodd"/></svg>
        luciabarrenechearuiz@correovela.mx
      </span>
    </div>
  </section>

</main>
</body>
</html>
```